Real Estate Agent need For Sale sign for

We need a for sale sign for our team based in Los Angeles, CA. My team name is Corvalen Real Estate Group. Also known as Team Corvalen. We are also under the Brandt Osgood umbrella. We are a real estate team that enjoys contributing to the world through supporting homeowners and sellers achieve their real estate goals. The final design should communicate trust, integrity, and loyalty.
Need to have our team name on there: Team Corvalen, phone number 323-555-0172, my licensed number DRE #8062714 on there. The size of the sign will be 32X36.
Target Market(s)
Home buyers and sellers.
Industry/Entity Type
Real Estate Agent
Colors
Designer to choose colors to be used in the design.
Look and feel

```html
<!DOCTYPE html>
<html lang="en">
<head>
<meta charset="utf-8">
<title>Corvalen Real Estate Group – For Sale Sign</title>
<link rel="stylesheet" href="https://fonts.googleapis.com/css2?family=Play:wght@400;700&display=swap">
<style>
  :root {
    --backdrop: #e9e7e3;
    --sign-white: #ffffff;
    --brand-red: #e8192c;
    --brand-blue: #0a57ac;
    --ink-dark: #3a3a3a;
    --partner-red: #b40f3a;
  }
  * { margin: 0; padding: 0; box-sizing: border-box; }
  html, body { width: 1200px; height: 2174px; overflow: hidden; }
  body {
    background: var(--backdrop);
    font-family: "Play", sans-serif;
    position: relative;
  }
  .sign {
    position: absolute;
    left: 50px;
    top: 470px;
    width: 1100px;
    height: 1234px;
    background: var(--sign-white);
    box-shadow: 0 6px 24px rgba(0,0,0,0.18);
  }
  .sign__header {
    position: absolute;
    left: 72px; top: 60px;
    width: 952px; height: 198px;
    background: var(--brand-red);
    border-radius: 22px;
    display: flex; align-items: center; justify-content: center;
  }
  .sign__headline {
    color: var(--sign-white);
    font-weight: 700;
    font-size: 176px;
    line-height: 1;
    letter-spacing: 2px;
  }
  .sign__brand {
    position: absolute;
    left: 0; top: 328px;
    width: 1100px; height: 636px;
    background: var(--brand-blue);
    display: flex; flex-direction: column; align-items: center; justify-content: center;
    color: var(--sign-white);
    font-weight: 700;
    text-align: center;
  }
  .brand-name__main { font-size: 210px; line-height: 1; letter-spacing: 2px; }
  .brand-name__sub { font-size: 84px; line-height: 1.1; text-transform: uppercase; letter-spacing: 2px; margin-top: 14px; }
  .sign__contact {
    position: absolute;
    left: 0; top: 964px;
    width: 1100px; height: 130px;
    background: var(--brand-red);
    display: flex; align-items: center; justify-content: center; gap: 26px;
    color: var(--sign-white);
  }
  .contact__icon { width: 82px; height: 82px; }
  .contact__phone { font-size: 116px; font-weight: 700; line-height: 1; letter-spacing: 2px; }
  .sign__footer {
    position: absolute;
    left: 0; top: 1094px;
    width: 1100px; height: 140px;
    display: flex; align-items: center; justify-content: space-between;
    padding: 0 44px;
  }
  .partner-name {
    color: var(--partner-red);
    font-weight: 700;
    font-size: 40px;
  }
  .license {
    font-size: 34px;
    font-weight: 700;
    color: var(--ink-dark);
  }
  .license__number { color: var(--brand-red); margin-left: 8px; }
</style>
</head>
<body>
  <main class="sign">
    <div class="sign__header">
      <span class="sign__headline">FOR SALE</span>
    </div>

    <div class="sign__brand">
      <span class="brand-name__main">Corvalen</span>
      <span class="brand-name__sub">Real Estate Group</span>
    </div>

    <div class="sign__contact">
      <svg class="contact__icon" viewBox="0 0 24 24" aria-hidden="true">
        <path fill="#ffffff" d="M6.6 10.8a15.1 15.1 0 0 0 6.6 6.6l2.2-2.2a1 1 0 0 1 1-.25 11.4 11.4 0 0 0 3.6.57 1 1 0 0 1 1 1V20a1 1 0 0 1-1 1A17 17 0 0 1 3 4a1 1 0 0 1 1-1h3.5a1 1 0 0 1 1 1c0 1.25.2 2.45.57 3.6a1 1 0 0 1-.25 1z"/>
        <path fill="none" stroke="#ffffff" stroke-width="1.6" stroke-linecap="round" d="M14.5 3.5a6 6 0 0 1 6 6M14.5 6.8a2.8 2.8 0 0 1 2.8 2.8"/>
      </svg>
      <span class="contact__phone">323-555-0172</span>
    </div>

    <div class="sign__footer">
      <span class="partner-name">Brandt Osgood</span>
      <span class="license">Licensed Number<span class="license__number">DRE #8062714</span></span>
    </div>
  </main>
</body>
</html>
```